Bref créative
Flyer, brochure, postcard
The Brennwick School
Where Curiosity Grows
This is a new high quality academic preschool from ages 6 weeks to pre-kindergarten. Early Childhood Campus. Logo and website were designed by Mark Forge; need to "brand" reputation for excellent early childhood education; by law all advertising must indicate it's opening August, 2012 or coming soon August 2012 somewhere on the flyer or postcard not on brochure;
Education
parents; families; caregivers with children under age 6; earning minimum of $75,000 per year; educated; both professionals and blue collar employees;
I would describe TBS by: exclusive, private, high quality, nurturing, loving, fun, building self-confidence in children, infants through pre-kindergarten; see website for more information and logo is provided; looking to "brand" a top notch reputation in early childhood education; we are different and want to stand out from other preschools; www.brennwickschool-example.com;
Content for Brochure
Content for Flyer

```html
<!DOCTYPE html>
<html lang="en">
<head>
<meta charset="utf-8">
<title>The Brennwick School – Brochure, Post Card, Flyer</title>
<link href="https://fonts.googleapis.com/css2?family=Libre+Baskerville:wght@400;700&family=Open+Sans:wght@400;600;700&display=swap" rel="stylesheet">
<style>
:root{
  --navy:#1b2d5c;
  --navy-deep:#0f1c40;
  --blue:#3d5f9e;
  --sky:#c9d8ee;
  --gold:#f3b41b;
  --gold-deep:#d99609;
  --paper:#ffffff;
  --ink:#2a2f3a;
  --stage:#ece6db;
  --photo-warm:#e8c9a8;
  --photo-cool:#b9c7dc;
  --photo-green:#b8c9a0;
}
*{box-sizing:border-box;margin:0;padding:0}
html,body{width:1200px;height:1088px;overflow:hidden;background:var(--stage)}
.board{position:relative;width:1200px;height:1088px;font-family:"Open Sans",Arial,sans-serif;color:var(--ink)}
.board-label{position:absolute;font-family:"Libre Baskerville",Georgia,serif;font-size:20px;color:var(--navy-deep)}
.piece{position:absolute;overflow:hidden;background:var(--paper);box-shadow:0 3px 10px rgba(0,0,0,.25)}
.panel{position:absolute;top:0;bottom:0;overflow:hidden}
.photo{position:absolute}
.photo.warm{background:linear-gradient(135deg,var(--photo-warm),#c99b78)}
.photo.cool{background:linear-gradient(135deg,var(--photo-cool),#8aa0c2)}
.photo.green{background:linear-gradient(135deg,var(--photo-green),#8ea36f)}
.photo.map{background:linear-gradient(135deg,#eef0ea,#d5dccf)}
.bar-heading{position:absolute;left:8px;right:8px;height:16px;background:linear-gradient(90deg,var(--gold),var(--gold-deep));color:var(--navy-deep);font-size:8px;font-weight:700;letter-spacing:.5px;padding:3px 6px;text-transform:uppercase}
.copy{position:absolute;left:10px;right:10px;font-size:5.4px;line-height:1.45;text-align:justify}
.copy p+p{margin-top:3px}
.on-navy{color:#e7ecf6}
.wordmark{font-family:"Libre Baskerville",Georgia,serif;font-weight:700;color:var(--paper);display:flex;align-items:center;gap:6px;line-height:1.05}
.wordmark .dot{width:12px;height:12px;border-radius:50%;background:var(--gold);flex:none}
.tagline{font-family:"Libre Baskerville",Georgia,serif;font-weight:700;color:var(--navy-deep);text-align:center}
.swoosh{position:absolute;left:0;width:100%}
.opening{font-family:"Libre Baskerville",Georgia,serif;font-weight:700;color:var(--gold);text-transform:uppercase;letter-spacing:1px}
.small-meta{font-size:6px;color:#6b7280}
</style>
</head>
<body>
<div class="board">

  <div class="board-label" style="left:552px;top:6px">Brochure</div>

  <!-- Brochure outside spread -->
  <section class="piece brochure-outside" style="left:30px;top:40px;width:550px;height:410px">
    <div class="panel" style="left:0;width:183px;background:linear-gradient(180deg,var(--navy),var(--navy-deep))">
      <div class="photo cool" style="left:0;top:0;width:183px;height:110px" role="img" aria-label="Photo of children playing in a classroom"></div>
      <div class="bar-heading" style="top:120px">About Us</div>
      <div class="copy on-navy" style="top:142px">
        <p>The Brennwick School is an academic preschool for children from six weeks to pre-kindergarten, built around small classes, caring teachers and a calm, bright campus where every child is known by name.</p>
        <p>Our teachers plan each day with play, reading, music and outdoor time so children grow in confidence, kindness and curiosity. Families are welcome partners in every step of the journey.</p>
        <p>Visit our campus to meet the staff, see the classrooms and learn how our early childhood program prepares little learners for school and for life.</p>
      </div>
      <svg class="swoosh" style="bottom:0" viewBox="0 0 183 60" height="60" preserveAspectRatio="none"><path d="M0 30 Q90 0 183 22 L183 60 L0 60Z" fill="var(--blue)"/><path d="M0 44 Q95 18 183 34 L183 40 Q95 26 0 50Z" fill="var(--gold)"/></svg>
    </div>
    <div class="panel" style="left:183px;width:184px;background:var(--paper)">
      <div class="photo warm" style="left:92px;top:0;width:92px;height:130px" role="img" aria-label="Photo of a child reaching up with a teacher"></div>
      <div class="copy" style="top:14px;right:100px;font-size:6px;text-align:left">
        <p><b>Early Childhood Campus</b></p>
        <p>4410 Larkfield Road, Suite 2<br>Dunmore Falls<br>(555) 014-2290</p>
      </div>
      <div class="photo map" style="left:12px;top:150px;width:160px;height:120px;border:1px solid #c9cfc2" role="img" aria-label="Street map showing the school location"></div>
      <div class="copy" style="top:285px;font-size:6px;text-align:center;color:var(--navy)">www.brennwickschool-example.com</div>
      <div class="photo cool" style="left:0;top:310px;width:184px;height:100px" role="img" aria-label="Photo of children gathered at a table"></div>
    </div>
    <div class="panel" style="left:367px;width:183px;background:var(--paper)">
      <div style="position:absolute;left:0;top:0;width:183px;height:92px;background:linear-gradient(180deg,var(--navy),var(--blue))"></div>
      <div class="wordmark" style="position:absolute;left:20px;top:30px;font-size:13px"><span class="dot"></span><span>THE BRENNWICK<br>SCHOOL</span></div>
      <div class="tagline" style="position:absolute;left:0;right:0;top:108px;font-size:10px">“Where Curiosity Grows”</div>
      <div class="photo warm" style="left:0;top:135px;width:183px;height:215px" role="img" aria-label="Photo of smiling preschool children with a teacher"></div>
      <svg class="swoosh" style="bottom:0" viewBox="0 0 183 80" height="80" preserveAspectRatio="none"><path d="M0 24 Q100 0 183 20 L183 80 L0 80Z" fill="var(--navy)"/><path d="M0 36 Q100 10 183 30 L183 37 Q100 18 0 44Z" fill="var(--gold)"/></svg>
    </div>
  </section>

  <!-- Brochure inside spread -->
  <section class="piece brochure-inside" style="left:610px;top:40px;width:560px;height:410px">
    <div class="panel" style="left:0;width:187px;background:linear-gradient(180deg,var(--navy),var(--navy-deep))">
      <div class="bar-heading" style="top:10px">Mission Statement</div>
      <div class="copy on-navy" style="top:32px">
        <p>We believe every child deserves a warm, safe and joyful place to begin learning. Our mission is to nurture the whole child through play, discovery and caring guidance.</p>
      </div>
      <div class="bar-heading" style="top:82px">Our Beliefs</div>
      <div class="copy on-navy" style="top:104px">
        <p>Children learn best when they feel loved and secure. We build self-confidence through small group work, hands-on projects and daily encouragement from trained teachers.</p>
        <p>We respect each family and keep parents close with daily notes, open visits and regular meetings about progress and goals.</p>
      </div>
      <div class="photo warm" style="left:0;top:280px;width:187px;height:130px" role="img" aria-label="Photo of a teacher reading with children"></div>
    </div>
    <div class="panel" style="left:187px;width:186px;background:var(--paper)">
      <div class="photo cool" style="left:0;top:0;width:186px;height:120px" role="img" aria-label="Photo of a toddler smiling at the camera"></div>
      <div class="bar-heading" style="top:130px">Curriculum &amp; Learning</div>
      <div class="copy" style="top:152px">
        <p>Our curriculum blends early literacy, number sense, science, art and music with plenty of outdoor play. Infants enjoy gentle routines while older children explore letters, shapes and stories.</p>
        <p>Each classroom is bright and well equipped, with low ratios so teachers can give every child the attention they need to thrive.</p>
      </div>
      <div class="photo warm" style="left:10px;top:290px;width:80px;height:110px" role="img" aria-label="Photo of a child painting"></div>
      <div class="photo green" style="left:96px;top:290px;width:80px;height:110px" role="img" aria-label="Photo of children playing outdoors"></div>
    </div>
    <div class="panel" style="left:373px;width:187px;background:var(--paper)">
      <div class="photo warm" style="left:0;top:0;width:93px;height:80px" role="img" aria-label="Photo of children in class"></div>
      <div class="photo cool" style="left:94px;top:0;width:93px;height:80px" role="img" aria-label="Photo of a child with building blocks"></div>
      <div class="bar-heading" style="top:90px">Hours &amp; Programs</div>
      <div class="copy" style="top:112px">
        <p>Open weekdays from early morning to evening. Full and part-time programs for infants, toddlers, preschool and pre-kindergarten.</p>
      </div>
      <div class="bar-heading" style="top:160px">How to Enroll</div>
      <div class="copy" style="top:182px">
        <p>Call or visit us to arrange a tour, meet our director and reserve a place for your child before our doors open.</p>
      </div>
      <div class="photo warm" style="left:0;top:240px;width:187px;height:170px" role="img" aria-label="Photo of two smiling young girls"></div>
    </div>
  </section>

  <div class="board-label" style="left:300px;top:470px">Post Card</div>
  <div class="board-label" style="left:880px;top:470px">Flyer</div>

  <!-- Post card front -->
  <section class="piece postcard-front" style="left:105px;top:510px;width:495px;height:270px">
    <div style="position:absolute;left:0;top:0;width:100%;height:78px;background:linear-gradient(180deg,var(--navy),var(--blue))"></div>
    <div class="wordmark" style="position:absolute;left:28px;top:20px;font-size:18px"><span class="dot" style="width:16px;height:16px"></span><span>THE BRENNWICK SCHOOL</span></div>
    <div class="small-meta" style="position:absolute;left:28px;top:86px;font-size:8px;color:var(--navy)">www.brennwickschool-example.com</div>
    <div class="tagline" style="position:absolute;left:0;right:0;top:100px;font-size:15px">“Where Curiosity Grows”</div>
    <div class="photo warm" style="left:200px;top:128px;width:295px;height:100px" role="img" aria-label="Photo of two smiling preschool girls"></div>
    <svg class="swoosh" style="bottom:0" viewBox="0 0 495 110" height="110" preserveAspectRatio="none"><path d="M0 20 Q200 70 495 50 L495 110 L0 110Z" fill="var(--navy)"/><path d="M0 34 Q210 80 495 60 L495 66 Q210 88 0 42Z" fill="var(--gold)"/></svg>
    <div class="opening" style="position:absolute;left:28px;bottom:14px;font-size:17px">Coming Soon August 2012</div>
  </section>

  <!-- Post card back -->
  <section class="piece postcard-back" style="left:105px;top:804px;width:495px;height:262px">
    <div class="photo cool" style="left:0;top:0;width:230px;height:150px" role="img" aria-label="Photo of a child smiling"></div>
    <div style="position:absolute;left:360px;top:18px;width:110px;height:34px;border:1px solid #9aa3b5;font-size:6px;text-align:center;padding-top:8px;color:#6b7280">Place Stamp<br>Here</div>
    <div style="position:absolute;left:260px;top:100px;width:210px">
      <div style="border-bottom:1px solid #b5bccb;height:18px"></div>
      <div style="border-bottom:1px solid #b5bccb;height:18px"></div>
      <div style="border-bottom:1px solid #b5bccb;height:18px"></div>
    </div>
    <svg class="swoosh" style="top:140px" viewBox="0 0 495 122" height="122" preserveAspectRatio="none"><path d="M0 30 Q240 0 495 26 L495 122 L0 122Z" fill="var(--navy)"/><path d="M0 40 Q240 10 495 34 L495 40 Q240 18 0 48Z" fill="var(--gold)"/></svg>
    <div class="wordmark" style="position:absolute;left:28px;top:200px;font-size:13px"><span class="dot"></span><span>THE BRENNWICK SCHOOL</span></div>
    <div style="position:absolute;left:28px;top:226px;font-size:7px;color:#e7ecf6;line-height:1.4">4410 Larkfield Road, Suite 2, Dunmore Falls · (555) 014-2290<br>www.brennwickschool-example.com</div>
  </section>

  <!-- Flyer -->
  <section class="piece flyer" style="left:654px;top:510px;width:516px;height:556px">
    <div style="position:absolute;left:0;top:0;width:100%;height:70px;background:linear-gradient(180deg,var(--navy),var(--blue))"></div>
    <div class="wordmark" style="position:absolute;left:26px;top:18px;font-size:18px"><span class="dot" style="width:16px;height:16px"></span><span>THE BRENNWICK SCHOOL</span></div>
    <div class="small-meta" style="position:absolute;left:26px;top:76px;font-size:8px;color:var(--navy)">www.brennwickschool-example.com</div>
    <div class="tagline" style="position:absolute;left:0;right:0;top:90px;font-size:15px">“Where Curiosity Grows”</div>
    <div class="photo warm" style="left:150px;top:114px;width:366px;height:130px" role="img" aria-label="Photo of two smiling preschool children"></div>
    <svg class="swoosh" style="top:200px" viewBox="0 0 516 60" height="60" preserveAspectRatio="none"><path d="M0 20 Q260 60 516 30 L516 60 L0 60Z" fill="var(--paper)"/><path d="M0 22 Q260 62 516 32 L516 38 Q260 66 0 28Z" fill="var(--gold)"/></svg>
    <div class="copy" style="top:262px;left:26px;right:26px;font-size:7px">
      <p>The Brennwick School is a community that promises early childhood education and builds a love of learning, making it the perfect place for your child's first steps in school. Our classrooms are warm, bright and thoughtfully planned for every age.</p>
      <p>The first five years of life shape the way a child learns, plays and grows. We focus on emotional, social and intellectual development, with teachers who know each child well and families who feel at home. From infants to pre-kindergarten, every day brings stories, songs, art, outdoor play and gentle routines that build confidence and curiosity.</p>
    </div>
    <div class="photo cool" style="left:26px;top:380px;width:150px;height:90px" role="img" aria-label="Photo of a toddler playing"></div>
    <div class="photo green" style="left:183px;top:380px;width:150px;height:90px" role="img" aria-label="Photo of children outdoors"></div>
    <div class="photo warm" style="left:340px;top:380px;width:150px;height:90px" role="img" aria-label="Photo of a teacher with a child"></div>
    <div style="position:absolute;left:0;bottom:0;width:100%;height:78px;background:linear-gradient(180deg,var(--blue),var(--navy-deep))"></div>
    <div class="opening" style="position:absolute;left:0;right:0;bottom:34px;text-align:center;font-size:22px">Coming Soon August 2012</div>
    <div style="position:absolute;left:0;right:0;bottom:12px;text-align:center;font-size:7px;color:#e7ecf6">4410 Larkfield Road, Suite 2, Dunmore Falls · (555) 014-2290 · www.brennwickschool-example.com</div>
  </section>

</div>
</body>
</html>
```